Geschäftspapier für Pfandhaus und Juwelier gesucht
Zielgruppe
Pfandhaus und Juwelier.
Aufgabenstellung
Ich betreibe mehrere Filialen und möchte all diese wir einem Briefkopf haben und ggf Platz für weitere da ich gerade 2 weitere eröffne. Unter www.leihhaus-Borlen.de sieht man Logo und Farben.
Ich möchte das Briefpapier als Datei haben und nicht gedruckt sondern will es selbst am Firmendrucker drucken.Die Bankverbindung sollte auch darauf sein aber erstmal etwas am Platzhalter eintragen .

```html
<!DOCTYPE html>
<html lang="de">
<head>
<meta charset="utf-8">
<title>Briefpapier Leihhaus Borlen</title>
<link href="https://fonts.googleapis.com/css2?family=Open+Sans:wght@400;600&family=Arimo:wght@400&display=swap" rel="stylesheet">
<style>
  :root {
    --backdrop: #ebebeb;
    --paper: #ffffff;
    --ink: #1f1f1f;
    --charcoal: #4a4846;
    --gold: #b29d62;
    --rule: #3a3a3a;
    --sig: #d9d9d9;
  }
  * { margin: 0; padding: 0; box-sizing: border-box; }
  html, body { width: 1200px; height: 1010px; overflow: hidden; background: var(--backdrop); }
  .letterhead {
    position: absolute; left: 260px; top: 24px; width: 680px; height: 962px;
    background: var(--paper); box-shadow: 0 4px 18px rgba(0,0,0,.12);
    font-family: "Open Sans", sans-serif; color: var(--ink);
  }
  .header-band { position: absolute; left: 300px; top: 24px; width: 312px; height: 8px; background: var(--gold); }
  .brand-block {
    position: absolute; left: 330px; top: 32px; width: 320px; height: 104px;
    background: var(--charcoal); display: flex; align-items: center; justify-content: center;
  }
  .brand-name { font-family: "Open Sans", sans-serif; font-weight: 600; font-size: 24px; color: var(--gold); letter-spacing: .5px; }
  .contact {
    position: absolute; left: 432px; top: 150px; padding-left: 12px;
    border-left: 1px solid var(--rule); font-size: 9px; line-height: 13px; font-style: normal;
  }
  .contact .address { margin-bottom: 5px; }
  .contact-row { display: flex; align-items: center; gap: 6px; }
  .contact-row svg { width: 8px; height: 8px; flex: none; }
  .sender-line {
    position: absolute; left: 76px; top: 262px; font-size: 7px;
    text-decoration: underline;
  }
  .recipient { position: absolute; left: 76px; top: 280px; font-size: 10.5px; line-height: 14px; }
  .fold-mark { position: absolute; left: 0; width: 20px; height: 1px; background: #bdbdbd; }
  .fold-mark.upper { top: 340px; }
  .fold-mark.lower { top: 644px; }
  .letter-body {
    position: absolute; left: 142px; top: 392px; width: 470px;
    font-family: "Arimo", Arial, sans-serif; font-size: 11.5px; line-height: 15px;
  }
  .letter-body .salutation { font-size: 12.5px; margin-bottom: 8px; }
  .letter-body p { margin-bottom: 14px; }
  .letter-body p:last-child { margin-bottom: 0; }
  .signature {
    position: absolute; left: 150px; top: 734px; width: 220px; height: 58px;
    background: linear-gradient(90deg, var(--sig), #ececec); border-radius: 4px;
  }
  .bank-details {
    position: absolute; left: 470px; top: 800px; padding-left: 12px;
    border-left: 1px solid var(--rule); font-size: 9.5px; line-height: 14px;
  }
  .bank-details .bank-name { margin-top: 5px; }
  .footer-band { position: absolute; left: 452px; top: 920px; width: 228px; height: 8px; background: var(--gold); }
</style>
</head>
<body>
  <main class="letterhead">
    <div class="header-band"></div>
    <div class="brand-block"><span class="brand-name">Leihhaus Borlen</span></div>

    <address class="contact">
      <div class="address">Matthias Borlen Leihhaus<br>Lindenallee 4<br>66113 Saarbrücken</div>
      <div class="contact-row"><svg viewBox="0 0 10 10"><path d="M2 1h2l1 2.5-1.2 1a5 5 0 0 0 2.7 2.7l1-1.2L10 7v2a1 1 0 0 1-1 1A9 9 0 0 1 0 2a1 1 0 0 1 1-1z" fill="#b29d62"/></svg>+49 (0) 681 55 210 400</div>
      <div class="contact-row"><svg viewBox="0 0 10 10"><rect x="1" y="3" width="8" height="6" fill="#b29d62"/><rect x="3" y="0.5" width="4" height="3" fill="#b29d62"/></svg>+49 (0) 681 55 210 409</div>
      <div class="contact-row"><svg viewBox="0 0 10 10"><rect x="0.5" y="2" width="9" height="6" fill="#b29d62"/><path d="M0.5 2l4.5 3.5L9.5 2" stroke="#fff" fill="none" stroke-width=".8"/></svg>info@leihhaus-borlen.de</div>
      <div class="contact-row"><svg viewBox="0 0 10 10"><circle cx="5" cy="5" r="4.5" fill="#b29d62"/></svg>www.leihhaus-Borlen.de</div>
    </address>

    <div class="sender-line">Matthias Borlen Leihhaus | Lindenallee 4 | 66113 Saarbrücken</div>
    <div class="recipient">Herr<br>Mark Mustermann<br>Musterweg 13<br>24102 Dortmund</div>

    <div class="fold-mark upper"></div>
    <div class="fold-mark lower"></div>

    <section class="letter-body">
      <div class="salutation">Herr Becker</div>
      <p>Lorem ipsum dolor sit amet, consectetur adipiscing elit. Proin tincidunt, lectus id malesuada cursus, lorem augue egestas magna, ut mattis orci ante ut arcu. Sed mauris tellus, fermentum quis ligula nec, posuere pulvinar eros. Nam at mi quis velit pellentesque finibus. Donec lacus velit, faucibus mollis dolor nec, finibus pellentesque orci. Duis sed dictum elit, ut posuere arcu. Phasellus ac dolor et ante consequat rutrum nec nec tortor. Donec consequat, nibh sit amet pulvinar faucibus, turpis magna venenatis diam, vel pretium eros erat vestibulum nulla.</p>
      <p>Sed pretium ac enim eu viverra. Aliquam ac est eget magna convallis convallis. Aenean augue purus, finibus eget turpis quis, finibus dignissim nibh. Phasellus viverra lobortis dignissim. Duis varius turpis in sapien accumsan facilisis. Sed vehicula gravida diam a interdum. Nullam convallis ligula id erat egestas consequat. Integer consectetur ex vel aliquet iaculis. Vestibulum molestie sodales mauris, at tincidunt risus pellentesqu.</p>
      <p>Mauris facilisis, lectus at accumsan tincidunt, dui magna imperdiet sem, quis tempor est lectus eu ipsum. Praesent in fermentum nisl. Maecenas at lorem at odio interdum iaculis. Pellentesque cursus nulla nunc, ut suscipit nulla maximus et. Donec maximus rhoncus metus, vel laoreet nisi pretium sit amet. Donec posuere enim lectus, vitae aliquam augue tincidunt dignissim. Morbi vitae congue velit, quis elementum.</p>
    </section>

    <div class="signature" role="img" aria-label="Handschriftliche Unterschrift von Matthias Borlen"></div>

    <div class="bank-details">
      <div>Bankverbindung:</div>
      <div>Matthias Borlen</div>
      <div class="bank-name">Nordbank Saar</div>
      <div>USt-ID-Nr. DEXXXXXXXX</div>
      <div>IBAN: DEXX XXXX XXXX XXXX XXXX X</div>
      <div>BIC: XXXXXXXX</div>
    </div>
    <div class="footer-band"></div>
  </main>
</body>
</html>
```